US company needs luxury product packaging design for a line of hair extensions

What we Need:
Design product packaging for our top of the line hair extension product called Velorina™, the design should have the Velorina™ name,and the head from our Plumestrand logo on the box.

Who we are
Our company PlumeStrand™ is a wholesaler of 100% human hair extensions. We sell the best quality double drawn hair wefts, clip-ins and wigs.

The detailed brief is in the attached word document with examples of packaging we like and we have also uploaded our company logo

The winning designer(s) will work with us on 9 other products packages that we need, so it is important to think strategically

Thanks

Target Market(s)

African American Women

Industry/Entity Type

Hair And Beauty

Font styles to use
Serif
Decorative
Script

Colors
fbf289
b768aa
e24096
000000
fbd4d5
f59195
ffc214
d3a5cc
eda3c7

Requirements
Must have
• Evoke luxury
Nice to have
• See Attached brief

```html
<!DOCTYPE html>
<html lang="en">
<head>
<meta charset="UTF-8">
<title>Velorina – Hair Care Instructions</title>
<link href="https://fonts.googleapis.com/css2?family=Nunito+Sans:wght@300;400;600&display=swap" rel="stylesheet">
<style>
  :root {
    --page-bg: #ffffff;
    --burgundy: #9e1445;
    --gold-light: #f7dc8a;
    --gold-mid: #d9aa3e;
    --gold-dark: #a8791f;
    --brand-gold: #d2a445;
    --text-light: #ffffff;
  }
  * { margin: 0; padding: 0; box-sizing: border-box; }
  html, body {
    width: 855px;
    height: 1200px;
    overflow: hidden;
    background: var(--page-bg);
  }
  .care-card {
    position: relative;
    width: 855px;
    height: 1200px;
    font-family: "Nunito Sans", Arial, sans-serif;
    color: var(--text-light);
  }
  .card-shape {
    position: absolute;
    left: 0;
    top: 0;
  }
  .brand-name {
    position: absolute;
    left: 142px;
    top: 236px;
    font-size: 78px;
    font-weight: 300;
    letter-spacing: 1px;
    color: var(--brand-gold);
    line-height: 1;
  }
  .instructions {
    position: absolute;
    left: 143px;
    top: 412px;
    width: 600px;
  }
  .instructions-title {
    font-size: 32px;
    font-weight: 600;
    line-height: 40px;
    margin-bottom: 25px;
  }
  .step-list {
    list-style: none;
  }
  .step {
    font-size: 29px;
    font-weight: 300;
    line-height: 40px;
    padding-left: 40px;
    text-indent: -40px;
    margin-bottom: 11px;
  }
</style>
</head>
<body>
  <main class="care-card">
    <svg class="card-shape" width="855" height="1200" viewBox="0 0 855 1200" aria-hidden="true">
      <defs>
        <linearGradient id="goldRibbon" x1="0" y1="0" x2="1" y2="0">
          <stop offset="0" stop-color="var(--gold-light)"/>
          <stop offset="0.35" stop-color="var(--gold-mid)"/>
          <stop offset="0.6" stop-color="var(--gold-dark)"/>
          <stop offset="0.85" stop-color="var(--gold-mid)"/>
          <stop offset="1" stop-color="var(--gold-light)"/>
        </linearGradient>
      </defs>
      <path class="gold-ribbon" fill="url(#goldRibbon)"
            d="M84,118 C200,78 330,90 450,160 C560,225 650,278 770,270 L770,292 C650,298 560,247 450,182 C330,114 200,102 84,140 Z"/>
      <path class="burgundy-panel" fill="var(--burgundy)"
            d="M84,138 C200,100 330,112 450,180 C560,245 650,296 770,290 L770,1118 L84,1118 Z"/>
    </svg>

    <div class="brand-name">Velorina</div>

    <section class="instructions">
      <h1 class="instructions-title">Hair Care Instructions:</h1>
      <ol class="step-list">
        <li class="step">1. When brushing Velorina, start at the ends and methodically work up towards the root using a weave brush</li>
        <li class="step">2. Shampoo hair using a mild moisturizing shampoo</li>
        <li class="step">3. After shampooing, rinse hair thoroughly with warm water and condition with your favorite conditioner</li>
        <li class="step">4. Blow dry or use any type dryer as you wish</li>
        <li class="step">5. Style as desired</li>
      </ol>
    </section>
  </main>
</body>
</html>
```